Vorn Apparel Brochure Project

Looking for a brochure to send out with samples of our apparel. The name of our company is Vorn Apparel and we are distributors for 7.42. I have attached an older 7.42 brochure. I would like the brochure to be regular paper size with no folds.

Target Market(s)

Buyers working for large U.S. retail stores

Colors

Designer to choose colors to be used in the design.

Requirements
Must have
• Must look sleek and professional.

```html
<!DOCTYPE html>
<html lang="en">
<head>
<meta charset="utf-8">
<title>Vorn Apparel Brochure</title>
<link href="https://fonts.googleapis.com/css2?family=Lato:wght@400;700&display=swap" rel="stylesheet">
<style>
  :root {
    --backdrop: #e6e4e3;
    --brand-red: #8a1719;
    --bright-red: #d01c24;
    --deep-red: #6e1013;
    --paper: #ffffff;
    --paper-shade: #e9e9ea;
    --ink: #1d1d1d;
    --on-red: #ffffff;
  }
  * { margin: 0; padding: 0; box-sizing: border-box; }
  html, body {
    width: 1200px; height: 901px; overflow: hidden;
    background: var(--backdrop);
    font-family: "Lato", sans-serif;
  }
  .spread {
    position: absolute; left: 64px; top: 58px;
    width: 1086px; height: 772px; display: flex;
    box-shadow: 0 4px 14px rgba(0,0,0,0.18);
  }
  .page { position: relative; height: 100%; overflow: hidden; }

  /* Back cover */
  .back-cover { width: 536px; background: var(--brand-red); color: var(--on-red); text-align: center; }
  .back-cover .brand-mark {
    position: absolute; left: 136px; top: 196px;
    width: 264px; height: 264px; border: 4px solid var(--on-red); border-radius: 50%;
    display: flex; align-items: center; justify-content: center;
  }
  .brand-name { font-weight: 700; color: var(--on-red); line-height: 1.1; }
  .back-cover .brand-name { font-size: 40px; }
  .back-cover .invitation { position: absolute; top: 552px; left: 0; width: 100%; font-size: 13px; line-height: 16px; }
  .back-cover .contact-line { position: absolute; top: 620px; left: 0; width: 100%; font-size: 18px; line-height: 23px; }
  .back-cover .address { position: absolute; top: 690px; left: 0; width: 100%; font-size: 12.5px; }

  /* Letter page */
  .letter-page { width: 550px; background: var(--paper); }
  .letter-page .swoosh { position: absolute; inset: 0; }
  .letter-page .brand-mark {
    position: absolute; left: 200px; top: 66px;
    width: 156px; height: 156px; border-radius: 50%;
    background: var(--brand-red); border: 3px solid var(--paper);
    box-shadow: 0 0 0 2px var(--brand-red);
    display: flex; align-items: center; justify-content: center; text-align: center;
  }
  .letter-page .brand-name { font-size: 24px; }
  .letter-body {
    position: absolute; left: 46px; top: 281px; width: 462px;
    font-size: 10.4px; line-height: 14.2px; color: var(--ink); text-align: justify;
  }
  .letter-body p { margin-bottom: 13px; }
  .letter-body .closing { margin-top: 44px; text-align: left; }
  .letter-page .address {
    position: absolute; right: 42px; top: 698px; text-align: right;
    color: var(--brand-red); font-size: 12.5px; line-height: 17px;
  }
</style>
</head>
<body>
<main class="spread">
  <section class="page back-cover">
    <div class="brand-mark"><span class="brand-name">Vorn<br>Apparel</span></div>
    <p class="invitation">We would love to talk with you about supplying<br>our artisan products to your establishment.<br>Please feel free to contact me via email at</p>
    <p class="contact-line">orders@vornapparel.com or cell<br>phone at 555-014-2290.</p>
    <p class="address">480 Harbor Bend Lane, Fairhaven, CA 90210</p>
  </section>

  <section class="page letter-page">
    <svg class="swoosh" width="550" height="772" viewBox="0 0 550 772" aria-hidden="true">
      <defs>
        <linearGradient id="redSweep" x1="0" y1="0" x2="1" y2="0">
          <stop offset="0" stop-color="#7a1215"/>
          <stop offset="0.6" stop-color="#9e1a1e"/>
          <stop offset="1" stop-color="#d8202a"/>
        </linearGradient>
        <linearGradient id="paperShade" x1="0" y1="0" x2="0" y2="1">
          <stop offset="0" stop-color="#ffffff"/>
          <stop offset="0.5" stop-color="#f6f6f6"/>
          <stop offset="1" stop-color="#e4e4e5"/>
        </linearGradient>
      </defs>
      <rect width="550" height="772" fill="url(#paperShade)"/>
      <path d="M0 0 H550 V62 C430 90 330 126 250 128 C160 130 70 96 0 72 Z" fill="url(#redSweep)"/>
      <path d="M0 72 C70 96 160 130 250 128 C330 126 430 92 550 66 V84 C430 112 330 150 250 152 C160 154 70 122 0 94 Z" fill="#d3d3d5" opacity="0.7"/>
      <path d="M0 88 C80 118 170 146 250 146 C340 146 440 110 550 96 V104 C440 120 340 158 250 160 C170 160 80 134 0 104 Z" fill="#c11c22"/>
      <path d="M0 610 C140 650 260 700 340 772 H0 Z" fill="#d01c24"/>
      <path d="M0 640 C130 672 230 716 290 772 H0 Z" fill="#8e1619"/>
      <path d="M0 690 C90 712 160 740 200 772 H0 Z" fill="#6e1013"/>
      <path d="M0 598 C150 636 280 690 370 772 H352 C270 700 140 648 0 614 Z" fill="#cfcfd1" opacity="0.8"/>
    </svg>
    <div class="brand-mark"><span class="brand-name">Vorn<br>Apparel</span></div>
    <div class="letter-body">
      <p>We proudly present the finest artisanal luxury, hand-spun and hand-woven (known as "khadi") fabric products, emphasizing the link between farmers, weavers, vegetable dyers and block printing traditions. This result is a coherent and meaningful fashion garment line that creates grounds for ethical products.</p>
      <p>Our clothes are 100% handmade by 7.42 artisans and we select the finest of fabrics for our designs including khadi denim, kala cotton (all organic), 200 count khadi cotton, silk and ahimsa silk. All cotton fabric used by 7.42 is 100% khadi cotton and dyed in 100% natural dyes.</p>
      <p>Khadi is an ideal choice for green and ethical clothing. Made from cotton, silk, wool and other natural fibers, these fabrics have been in existence for hundreds of years. Today the production of khadi provides sustenance to millions of people in India. About eighty percent of khadi artisans are women, often from some of the poorest communities in the country.</p>
      <p>Our fabric simply looks beautiful. It is a labor of love. It's about human beings working with nature and transforming natural materials into beautiful wearable clothing.</p>
      <p class="closing">We would love to talk with you about supplying our artisan products to your establishment. Please feel free to contact me via email at orders@vornapparel.com or cell phone at 555-014-2290.</p>
    </div>
    <p class="address">480 Harbor Bend Lane,<br>Fairhaven, CA 90210</p>
  </section>
</main>
</body>
</html>
```